Meditation class design

I need a flyer design for a new meditation class based in Narellan NSW. The information that I want on the flyer is:
'THE QUIET HARBOUR'
Awaken to your purpose. Guiding you to your true divinity.
Allow yourself to invest time for YOU.
Clear the mind with stillness and learn to live in the NOW.
BENEFITS: Balance
Healing the Mind, Body & Spirit
Creates Peace & calmness
Self development
Happiness
Letting go to what is
Clearer mind
Keeps you looking young
Answers
Enriching your life by excepting & embracing who you are
Picture in the whole background of a person sitting down crossed legged looking into the sun with a butterfly around in the distance. Colours to use is shades of purple, white, shades of pink.

I don't need any more designs for my flyer. Can anyone help me to get my file that Pell has created for me.  I have downloaded it but can't see it.

Thank you

REGARDS

MORGAN VELQUIST

• TIME: 10am to 11am
WHERE: Kestrel Fitness Hub, Unit 2
3-5 Wattleby Creek Lane
Narellan NSW
PRICE: $15.00

'ENHANCING THE QUALITY OF YOUR LIFE & THOSE AROUND YOU'

Contact Morgan on 0498 362 105
Email: corvintesa@ripplenet.com
Facebook: Ember Path Wellness

```html
<!DOCTYPE html>
<html lang="en">
<head>
<meta charset="utf-8">
<title>The Quiet Harbour – Meditation Class Flyer</title>
<link href="https://fonts.googleapis.com/css2?family=Great+Vibes&family=Tinos:ital,wght@0,400;0,700;1,700&family=Arimo:wght@400;700&display=swap" rel="stylesheet">
<style>
  :root {
    --backdrop: #8a8a8a;
    --purple-deep: #5e0f8c;
    --purple: #7a1fb0;
    --purple-title: #6a1b9a;
    --plum-text: #5c155f;
    --pink-light: #f3d9f0;
    --pink-mid: #e7b3e4;
    --pink-soft: #f9ecf8;
    --white: #ffffff;
    --ink: #111111;
  }
  * { margin: 0; padding: 0; box-sizing: border-box; }
  html, body { width: 952px; height: 1200px; overflow: hidden; }
  body { background: var(--backdrop); position: relative; }

  .flyer {
    position: absolute;
    left: 45px; top: 39px;
    width: 725px; height: 937px;
    transform: scale(1.19);
    transform-origin: top left;
    overflow: hidden;
    background: radial-gradient(ellipse at 40% 35%, var(--white) 0%, var(--pink-soft) 35%, var(--pink-light) 65%, var(--pink-mid) 100%);
    box-shadow: 4px 4px 8px rgba(0,0,0,0.45);
  }
  .flyer__shapes { position: absolute; inset: 0; width: 725px; height: 937px; }

  .photo-area {
    position: absolute;
    left: 300px; top: 265px;
    width: 425px; height: 570px;
    background: radial-gradient(ellipse at 50% 55%, rgba(255,255,255,0.95) 0%, rgba(250,236,246,0.8) 45%, rgba(235,190,230,0) 75%);
  }

  .title {
    position: absolute;
    font-family: "Great Vibes", cursive;
    color: var(--purple-title);
    text-shadow: 2px 2px 2px rgba(255,255,255,0.9), 3px 3px 4px rgba(80,20,90,0.35);
    line-height: 1;
    white-space: nowrap;
  }
  .title--top { left: 380px; top: 52px; width: 330px; text-align: center; font-size: 76px; }
  .title--bottom { left: 360px; top: 160px; width: 360px; text-align: center; font-size: 90px; }

  .headline {
    position: absolute;
    left: 0; top: 280px; width: 432px;
    font-family: "Tinos", serif;
    font-weight: 700; font-style: italic;
    font-size: 34px; line-height: 45px;
    text-align: center;
    color: var(--plum-text);
    text-shadow: 2px 2px 2px rgba(255,255,255,0.9);
  }

  .intro {
    position: absolute;
    left: 18px; top: 502px;
    font-family: "Arimo", sans-serif;
    font-weight: 700;
    font-size: 18.5px; line-height: 29px;
    color: var(--ink);
  }

  .benefits { position: absolute; left: 18px; top: 574px; font-family: "Arimo", sans-serif; color: var(--ink); }
  .benefits__heading { font-family: "Tinos", serif; font-weight: 700; font-size: 26px; line-height: 34px; }
  .benefits__list { list-style: none; margin-top: 4px; }
  .benefits__item { position: relative; padding-left: 14px; font-size: 14.5px; line-height: 20px; font-weight: 700; color: #1c1c1c; }
  .benefits__item::before {
    content: ""; position: absolute; left: 0; top: 6px;
    width: 8px; height: 8px; border-radius: 50%;
    background: var(--purple);
  }

  .details {
    position: absolute;
    left: 428px; top: 664px;
    width: 300px; height: 118px;
    padding: 8px 10px;
    background: rgba(255,255,255,0.92);
    border: 1.5px solid var(--purple);
    border-radius: 14px 0 0 14px;
    font-family: "Tinos", serif;
    font-size: 15px; line-height: 19.5px;
    color: var(--ink);
  }
  .details__label { font-weight: 700; color: var(--purple); }

  .tagline {
    position: absolute;
    left: 0; top: 852px; width: 725px;
    font-family: "Tinos", serif;
    font-size: 30px; line-height: 40px;
    text-align: center;
    color: var(--white);
    text-shadow: 2px 2px 3px rgba(40,0,60,0.75);
  }
</style>
</head>
<body>
  <main class="flyer">
    <svg class="flyer__shapes" viewBox="0 0 725 937" aria-hidden="true">
      <defs>
        <linearGradient id="band-top" x1="0" y1="0" x2="1" y2="0">
          <stop offset="0" stop-color="#8a25c0"/>
          <stop offset="0.5" stop-color="#6a12a0"/>
          <stop offset="1" stop-color="#9a3ac8"/>
        </linearGradient>
        <linearGradient id="band-bottom" x1="0" y1="0" x2="1" y2="0">
          <stop offset="0" stop-color="#7a1fb0"/>
          <stop offset="0.5" stop-color="#d38ad6"/>
          <stop offset="1" stop-color="#6a14a6"/>
        </linearGradient>
        <linearGradient id="sky-top" x1="0" y1="0" x2="0" y2="1">
          <stop offset="0" stop-color="#dc8fdc"/>
          <stop offset="1" stop-color="#f4d6f1"/>
        </linearGradient>
      </defs>
      <path d="M0 0 H725 V40 C600 10 480 20 380 50 C250 90 120 110 0 95 Z" fill="url(#sky-top)"/>
      <path d="M0 95 C120 110 250 90 380 50 C480 20 600 10 725 40 V58 C610 30 500 40 400 75 C260 130 120 150 0 135 Z" fill="url(#band-top)"/>
      <path d="M0 135 C120 150 260 130 400 75 C500 40 610 30 725 58 V64 C610 40 500 52 410 85 C270 140 120 165 0 152 Z" fill="#ffffff"/>
      <path d="M0 790 C200 830 500 830 725 790 V937 H0 Z" fill="#ffffff"/>
      <path d="M0 800 C200 842 500 842 725 800 V937 H0 Z" fill="url(#band-bottom)"/>
    </svg>

    <div class="photo-area" role="img" aria-label="Photograph of a woman in a white robe meditating cross-legged with eyes closed"></div>

    <h1 class="title title--top">The Quiet</h1>
    <div class="title title--bottom">Harbour</div>

    <p class="headline">Awaken to your purpose. Guiding you to your true divinity. Allow yourself to invest time for YOU.</p>

    <p class="intro">Clear the mind with stillness<br>and learn to live in the NOW.</p>

    <section class="benefits">
      <h2 class="benefits__heading">BENEFITS:</h2>
      <ul class="benefits__list">
        <li class="benefits__item">Balance</li>
        <li class="benefits__item">Healing the Mind, Body &amp; Spirit</li>
        <li class="benefits__item">Creates Peace &amp; calmness</li>
        <li class="benefits__item">Self development</li>
        <li class="benefits__item">Happiness</li>
        <li class="benefits__item">Letting go to what is</li>
        <li class="benefits__item">Clearer mind</li>
        <li class="benefits__item">Keeps you looking young</li>
      </ul>
    </section>

    <div class="details">
      <div><span class="details__label">TIME:</span> 10am to 11am</div>
      <div><span class="details__label">WHERE:</span> Kestrel Fitness Hub, Unit 2</div>
      <div>3-5 Wattleby Creek Lane</div>
      <div>Narellan NSW</div>
      <div class="details__label">PRICE: $15.00</div>
    </div>

    <p class="tagline">ENHANCING THE QUALITY OF YOUR<br>LIFE &amp; THOSE AROUND YOU</p>
  </main>
</body>
</html>
```